Not Your Average Diet Book Cover Design

I need a book cover designed for a project titled:
Title: Quiet Harbor Method
Sub-title: The Gentle Road To Lasting Change With Your Plate
Author: Darlene Forsythe
Designation: Not a Doctor
The book is a look at 8 trendy diets (Brevard, Whole Foods, Paleo, Keto, Mediterranean, Sugar Free, Alkaline and Intermittent Fasting), with each chapter covering the pros and cons of one.
The theme throughout the book is that, when approached as a diet, they are each doomed to failure. When sustainability and lifestyle are taken into consideration, however, any one of them (or a combination of two or more) can lead to overall health and weight management.
Vegetables, mindset and habit creation are 3 of the "overlap" factors implied in the title.
I have uploaded a temporary cover that I am using as a placeholder at the moment. I do NOT want anything like it. (Use the tagline above, not the one in the sample cover).
Please, NO images of scales, stomachs, or anything else that is super cliche for the weight loss industry.
This is a full length book, written in a conversation tone, that I want to stand out from the a) copy and pasted online "experts" and b) doctors and fitpros who think it's their way or the highway. I want it to be welcoming and accessible.
I want the book to appeal to an audience who is currently struggling with their health and most likely failed at many diets in the past.
I will need a print cover for a 6"x 9" Printloom book, as well as a Veltra cover and an Tavrel cover.
I would like all source files, including any fonts used. For delivery, placeholder text can be used for the back cover.
Target Market(s)
Male & Female
Overweight
Unhealthy, but not severely so
Have tried diets before and failed
Age: 25-55 (average)
Income: $30-50k USD
Marital status: Single OR not entirely satisfied with the relationship
Location: Canada, USA, Australia, UK
Industry/Entity Type
Health And Wellness
Colors
Designer to choose colors to be used in the design.
Requirements
Must have
- Title: Quiet Harbor Method
- Sub-title: The Gentle Road To Lasting Change With Your Plate
- Author: Darlene Forsythe
- Designation: Not a Doctor
Nice to have
- A welcoming, understanding feeling
- Implications of holistic health
Should not have
- Images:
- - Scale or measuring tapes, etc
- - stomachs/abs
- - yoga or any silhouettes
- A look similar to the sample.

```html
<!DOCTYPE html>
<html lang="en">
<head>
<meta charset="UTF-8">
<title>Quiet Harbor Method — Book Cover</title>
<link rel="stylesheet" href="https://fonts.googleapis.com/css2?family=Yellowtail&family=Poppins:wght@300;500&display=swap">
<style>
  :root {
    --page-bg: #ececec;
    --cover-lime: #eaf68c;
    --cover-lime-deep: #d9f07e;
    --cover-green: #a9e39b;
    --mint: #8fdfa8;
    --ink: #2f3a36;
    --white: #ffffff;
  }
  * { margin: 0; padding: 0; box-sizing: border-box; }
  html, body {
    width: 1200px; height: 800px; overflow: hidden;
    background: var(--page-bg);
  }
  .stage { position: relative; width: 1200px; height: 800px; }
  .cover {
    position: absolute; left: 360px; top: 40px;
    width: 480px; height: 720px; overflow: hidden;
    background: var(--cover-lime);
  }
  .cover-pattern {
    position: absolute; inset: 0;
    background: linear-gradient(180deg, var(--cover-lime) 0%, var(--cover-lime-deep) 62%, var(--cover-green) 100%);
  }
  .title-blob { position: absolute; left: 40px; top: 110px; width: 380px; height: 300px; }
  .title {
    position: absolute; left: 0; top: 130px; width: 480px;
    font-family: "Yellowtail", cursive; font-weight: 400;
    color: var(--ink); text-align: center; line-height: 0.95;
    transform: rotate(-3deg);
  }
  .title span { display: block; }
  .title .line-1 { font-size: 78px; margin-left: -30px; }
  .title .line-2 { font-size: 62px; margin-left: 10px; }
  .title .line-3 { font-size: 82px; margin-left: 30px; }
  .subtitle-band {
    position: absolute; left: 0; top: 384px; width: 480px; height: 114px;
    background: var(--mint);
    display: flex; flex-direction: column; justify-content: center; align-items: center;
    font-family: "Poppins", sans-serif; font-weight: 300; color: var(--white);
    text-align: center; line-height: 1.2;
  }
  .subtitle-band .sub-1 { font-size: 24px; }
  .subtitle-band .sub-2 { font-size: 31px; }
  .author {
    position: absolute; left: 0; top: 612px; width: 480px; text-align: center;
    font-family: "Poppins", sans-serif; font-weight: 500; color: var(--ink);
    font-size: 38px; letter-spacing: 0.5px;
  }
  .designation {
    position: absolute; left: 0; top: 666px; width: 480px; text-align: center;
    font-family: "Poppins", sans-serif; font-weight: 500; color: var(--ink);
    font-size: 18px; letter-spacing: 0.5px;
  }
</style>
</head>
<body>
<main class="stage">
  <section class="cover">
    <div class="cover-pattern" role="img" aria-label="Hand-drawn outline pattern of vegetables, fruits and mood faces in blue line on a lime background"></div>

    <svg class="title-blob" viewBox="0 0 380 300" aria-hidden="true">
      <path fill="#8fdfa8" d="M70 40 C110 5 160 25 200 15 C250 0 300 20 320 60 C345 100 370 120 360 170 C350 215 375 250 340 280 C300 305 250 270 200 285 C150 300 100 290 70 260 C35 230 10 200 20 150 C30 110 35 70 70 40 Z"/>
      <circle cx="355" cy="70" r="14" fill="#8fdfa8"/>
      <circle cx="22" cy="250" r="10" fill="#8fdfa8"/>
    </svg>

    <h1 class="title">
      <span class="line-1">Quiet</span>
      <span class="line-2">Harbor</span>
      <span class="line-3">Method</span>
    </h1>

    <div class="subtitle-band">
      <p class="sub-1">The Gentle Road To Lasting</p>
      <p class="sub-2">Change With Your Plate</p>
    </div>

    <p class="author">DARLENE FORSYTHE</p>
    <p class="designation">NOT A DOCTOR</p>
  </section>
</main>
</body>
</html>
```